Book Cover - For Best Selling Diet

Hi
Book cover required for a diet book being marketed to become a best seller
For best quality, image will be 2820 pixels on the shortest side and 4500 pixels on the longest side .
The book name : Bright Morning Plan
By Corinna Plett
( will add in the extra text once we see design - top and bottom subtitle )
I do not want a photo of a person on the book.
PLEASE SEE " THE 9 STEP FRAME" by Ned Galbury as an example of solid style and I also love Quiet Ledger for the font.
Branding Colours:
#F26432
#A4195C
#A7D8CC
Font that runs through our brand is : helvetica neue
This is for a book that will be marketed for #1 bestseller - So please only quality
designs that are designed in a unique style.
Thanks
Target Market(s)
Busy Working Mums, Affluent, 30+ .
Look and feel

```html
<!DOCTYPE html>
<html lang="en">
<head>
<meta charset="utf-8">
<title>Bright Morning Plan — Corinna Plett</title>
<link rel="stylesheet" href="https://fonts.googleapis.com/css2?family=Josefin+Sans:wght@300;400&family=Josefin+Slab:wght@400&display=swap">
<style>
  :root {
    --cover-orange: #F26432;
    --cover-white: #FFFFFF;
  }
  * { margin: 0; padding: 0; box-sizing: border-box; }
  html, body {
    width: 752px;
    height: 1200px;
    overflow: hidden;
    background: var(--cover-orange);
  }
  .book-cover {
    position: relative;
    width: 752px;
    height: 1200px;
    background: var(--cover-orange);
    color: var(--cover-white);
  }
  .book-title {
    position: absolute;
    left: 0;
    right: 0;
    top: 270px;
    text-align: center;
    font-family: "Josefin Sans", sans-serif;
    font-weight: 400;
    text-transform: uppercase;
    line-height: 1;
  }
  .book-title__line {
    display: block;
    white-space: nowrap;
  }
  .book-title__line--first {
    font-size: 136px;
    letter-spacing: 2px;
  }
  .book-title__line--second {
    margin-top: 52px;
    font-size: 104px;
    letter-spacing: 2px;
  }
  .book-title__line--third {
    margin-top: 54px;
    font-size: 178px;
    letter-spacing: 4px;
  }
  .book-author {
    position: absolute;
    right: 68px;
    top: 1080px;
    font-family: "Josefin Slab", serif;
    font-weight: 400;
    font-size: 38px;
    letter-spacing: 1px;
    white-space: nowrap;
  }
</style>
</head>
<body>
  <main class="book-cover">
    <h1 class="book-title">
      <span class="book-title__line book-title__line--first">Bright</span>
      <span class="book-title__line book-title__line--second">Morning</span>
      <span class="book-title__line book-title__line--third">Plan</span>
    </h1>
    <p class="book-author">Corinna Plett</p>
  </main>
</body>
</html>
```